One page flyer for nonprofit focused IT company

I need a one page flyer (one side of a single 8.5x11 page) with text and graphics. The company logo is already done, and it must appear on the flyer along with other icons and graphics. The final design will be printed on heavy weight glossy paper as a handout and also distributed as a PDF.

The text is provided in an attachment, if it needs to be shortened let me know.

Industry/Entity Type

Information Technology

Requirements
Must have
• some flare (colors, icons or images)
Should not have
• While we work for nonprofits, my company is a FOR PROFIT company.

```html
<!DOCTYPE html>
<html lang="en">
<head>
<meta charset="UTF-8">
<title>Meridian Systems Corporation – Nonprofit IT Services</title>
<link href="https://fonts.googleapis.com/css2?family=Montserrat:wght@600;700;800&family=Mulish:ital,wght@0,400;0,800;1,800&display=swap" rel="stylesheet">
<style>
:root{
  --maroon:#8e1a2b;
  --ink:#2a2a2a;
  --white:#ffffff;
  --hero-deep:#0c1a2a;
  --hero-mid:#1d6fa3;
  --hero-light:#3aa3d8;
}
*{margin:0;padding:0;box-sizing:border-box}
html,body{width:869px;height:1200px;overflow:hidden;background:var(--white)}
.flyer{position:relative;width:869px;height:1200px;background:var(--white);font-family:"Mulish",sans-serif;color:var(--ink);overflow:hidden}
.hero-art{position:absolute;left:0;top:0}
.brand{position:absolute;left:30px;top:88px;width:240px;text-align:center;font-family:"Montserrat",sans-serif;font-weight:700;color:var(--maroon);font-size:20px;line-height:22px;letter-spacing:.3px}
.anniversary{position:absolute;left:35px;top:140px;font-family:"Montserrat",sans-serif;font-weight:800;color:var(--maroon)}
.anniversary-number{font-size:104px;line-height:94px;letter-spacing:-4px}
.anniversary-label{font-size:23px;line-height:31px}
.portrait{position:absolute;left:63px;top:348px;width:194px;height:194px;border-radius:50%;border:6px solid var(--white);background:radial-gradient(circle at 50% 70%,#2f6fae 0%,#1b2b40 45%,#0d1117 100%)}
.hero-copy{position:absolute;left:324px;top:396px;width:496px;color:var(--white);text-align:center}
.hero-title{font-family:"Montserrat",sans-serif;font-weight:800;font-size:17.5px;line-height:24px}
.hero-text{margin-top:16px;font-size:11.1px;line-height:17.5px;text-align:justify;text-align-last:center}
.solutions{position:absolute;left:30px;top:547px;width:330px}
.section-head{display:flex;align-items:center;gap:12px;font-family:"Montserrat",sans-serif;font-weight:800;font-size:27px;color:var(--maroon)}
.solutions>.section-head{margin-top:23px}
.section-icon{width:43px;height:43px;border:1.5px solid var(--maroon);border-radius:50%;display:flex;align-items:center;justify-content:center}
.service{position:absolute;left:9px;width:316px}
.service-title{display:flex;align-items:center;gap:10px;font-family:"Montserrat",sans-serif;font-weight:800;font-size:12.2px;color:var(--maroon);line-height:14px}
.service-icon{flex:none;width:22px;height:22px;border:1.3px solid var(--maroon);border-radius:50%;display:flex;align-items:center;justify-content:center}
.service-text{margin-top:5px;font-size:9.4px;line-height:14.2px;text-align:justify}
.contact{position:absolute;left:0;bottom:0;width:440px;height:84px}
.contact-pill{position:absolute;left:30px;top:-12px;width:301px;height:34px;border:2.5px solid var(--maroon);border-radius:17px;background:var(--white);display:flex;align-items:center;justify-content:center;font-size:11.5px;color:var(--maroon)}
.contact-details{position:absolute;left:52px;top:32px;font-family:"Montserrat",sans-serif;font-weight:800;font-size:17px;line-height:23px;color:var(--white)}
.successes{position:absolute;left:438px;top:572px;width:390px;height:593px;background:var(--maroon);border-radius:0 0 30px 30px;color:var(--white);padding:52px 36px 0 36px}
.successes .section-head{color:var(--white);font-size:32px;gap:15px}
.successes .section-icon{width:52px;height:52px;border:2px solid var(--white)}
.case-title{font-family:"Montserrat",sans-serif;font-weight:800;font-size:13.2px;line-height:17px;padding-left:67px}
.case-title-first{display:flex;align-items:center;gap:14px;padding-left:0}
.case-ring{flex:none;width:36px;height:36px;border:1.5px solid var(--white);border-radius:50%}
.case-text{font-size:10.5px;line-height:14.5px;text-align:justify}
.case-text em{font-weight:800}
</style>
</head>
<body>
<main class="flyer">

  <svg class="hero-art" width="869" height="1200" viewBox="0 0 869 1200" role="img" aria-label="Photo of a businessman holding a tablet with a glowing network of cloud, globe, phone and growth chart graphics">
    <defs>
      <linearGradient id="heroFill" x1="1" y1="0" x2="0" y2="1">
        <stop offset="0" stop-color="var(--hero-light)"/>
        <stop offset=".5" stop-color="var(--hero-mid)"/>
        <stop offset="1" stop-color="var(--hero-deep)"/>
      </linearGradient>
    </defs>
    <path d="M477,0 L869,0 L869,562 C700,568 480,555 300,528 C240,515 215,440 222,360 C235,220 330,90 477,0 Z" fill="url(#heroFill)"/>
  </svg>
  <svg class="hero-art" width="869" height="1200" viewBox="0 0 869 1200" aria-hidden="true">
    <path d="M452,0 L470,0 C330,95 230,210 200,336 C204,200 300,90 452,0 Z" fill="var(--maroon)"/>
    <path d="M232,515 C300,550 500,572 869,564 L869,588 C500,598 300,582 232,515 Z" fill="var(--maroon)"/>
  </svg>

  <div class="brand">Meridian Systems<br>Corporation</div>

  <div class="anniversary">
    <div class="anniversary-number">50</div>
    <div class="anniversary-label">YEARS OF<br>NONPROFIT<br>IT SERVICES</div>
  </div>

  <div class="portrait" role="img" aria-label="Photo of a businessman in a suit holding a tablet projecting a world map network"></div>

  <section class="hero-copy">
    <h1 class="hero-title">AN EFFICIENT AND ELEGANT APPROACH<br>TO IT SOLUTION IMPLEMENTATIONS</h1>
    <p class="hero-text">Meridian Systems Corporation has been supporting the Information Systems needs of nonprofits for over 50 years. We continually strive to bring the latest technologies and best practices to nonprofits to drive down the cost of IT while implementing systems that drive revenue.</p>
  </section>

  <section class="solutions">
    <h2 class="section-head">
      <span class="section-icon"><svg width="18" height="22" viewBox="0 0 16 18"><path d="M8 1a5.5 5.5 0 0 0-3.2 10v2.5h6.4V11A5.5 5.5 0 0 0 8 1Z M5.5 15.5h5 M6.5 17h3" fill="none" stroke="var(--maroon)" stroke-width="1.3"/></svg></span>
      SOLUTIONS
    </h2>

    <article class="service" style="top:87px">
      <h3 class="service-title"><span class="service-icon"><svg width="12" height="10" viewBox="0 0 12 10"><rect x="1" y="1" width="10" height="7" fill="none" stroke="var(--maroon)" stroke-width="1.2"/></svg></span>WEB APPLICATIONS</h3>
      <p class="service-text">With a focus on non-profit websites and web based applications, MSC helps nonprofits communicate with their members and donors while maximizing online giving and engagement</p>
    </article>

    <article class="service" style="top:171px">
      <h3 class="service-title"><span class="service-icon"><svg width="8" height="12" viewBox="0 0 8 12"><rect x="1" y="1" width="6" height="10" rx="1" fill="none" stroke="var(--maroon)" stroke-width="1.2"/></svg></span>MOBILE APPLICATIONS</h3>
      <p class="service-text">Meridian Systems Corporation implements mobile applications for Zephyr phones and Pulsar OS to provide direct communications with members and donors enabling real-time, two-way interaction</p>
    </article>

    <article class="service" style="top:255px">
      <h3 class="service-title"><span class="service-icon"><svg width="12" height="12" viewBox="0 0 12 12"><circle cx="6" cy="6" r="3" fill="none" stroke="var(--maroon)" stroke-width="2.4" stroke-dasharray="2 1.4"/></svg></span>SYSTEMS INTEGRATION</h3>
      <p class="service-text">IT applications can get scattered and disconnected. Meridian Systems Corporation has decades of experience integrating these applications into a single cohesive system.</p>
    </article>

    <article class="service" style="top:338px">
      <h3 class="service-title"><span class="service-icon"><svg width="10" height="12" viewBox="0 0 10 12"><ellipse cx="5" cy="2.5" rx="4" ry="1.5" fill="none" stroke="var(--maroon)" stroke-width="1.1"/><path d="M1 2.5v7c0 .8 1.8 1.5 4 1.5s4-.7 4-1.5v-7 M1 6c0 .8 1.8 1.5 4 1.5S9 6.8 9 6" fill="none" stroke="var(--maroon)" stroke-width="1.1"/></svg></span>MEMBER DONOR DATABASE</h3>
      <p class="service-text">Meridian Systems Corporation’s GiveBase Member / Donor CRM system is fully customized for each client meeting the unique needs of your organization</p>
    </article>

    <article class="service" style="top:421px">
      <h3 class="service-title"><span class="service-icon"><svg width="13" height="9" viewBox="0 0 13 9"><path d="M3.5 8a2.5 2.5 0 0 1 0-5 3.5 3.5 0 0 1 6.5 .8A2 2 0 0 1 10 8Z" fill="none" stroke="var(--maroon)" stroke-width="1.1"/></svg></span>CLOUD MIGRATION</h3>
      <p class="service-text">Reduce IT costs by migrating to the latest cloud solutions</p>
    </article>

    <article class="service" style="top:469px">
      <h3 class="service-title"><span class="service-icon"><svg width="10" height="12" viewBox="0 0 10 12"><ellipse cx="5" cy="2.5" rx="4" ry="1.5" fill="none" stroke="var(--maroon)" stroke-width="1.1"/><path d="M1 2.5v7c0 .8 1.8 1.5 4 1.5s4-.7 4-1.5v-7 M1 6c0 .8 1.8 1.5 4 1.5S9 6.8 9 6" fill="none" stroke="var(--maroon)" stroke-width="1.1"/></svg></span>BUSINESS INTELLIGENCE<br>AND REPORTING</h3>
      <p class="service-text" style="margin-top:2px">Meridian Systems Corporation can wrestle all of an organization's data into simple executive dashboards and reports</p>
    </article>
  </section>

  <footer class="contact">
    <svg width="440" height="84" viewBox="0 0 440 84" style="position:absolute;left:0;top:0" aria-hidden="true">
      <path d="M0,0 L373,0 L425,84 L0,84 Z" fill="var(--maroon)"/>
    </svg>
    <div class="contact-pill">Contact Meridian Systems Corporation at</div>
    <div class="contact-details">info@meridiansys.example<br>555-014-2200 x306</div>
  </footer>

  <section class="successes">
    <h2 class="section-head">
      <span class="section-icon"><svg width="26" height="22" viewBox="0 0 26 22"><path d="M2 18 L9 11 L14 15 L23 5 M18 5h5v5" fill="none" stroke="var(--white)" stroke-width="2"/></svg></span>
      SUCCESSES
    </h2>

    <article class="case" style="margin-top:12px">
      <h3 class="case-title case-title-first"><span class="case-ring"></span>90% REDUCTION IN SOFTWARE<br>DEVELOPMENT COSTS</h3>
      <p class="case-text" style="margin-top:14px">National Motor Dealers Guild Value Guide needed to update its core product they engaged their in-house IT department who estimated the project would take 3 years and cost $3,000,000. NMDG decided to work with Meridian Systems Corporation instead, and the product was released to production in only 9 months at <em>one-tenth of the cost</em>, only $300,000</p>
    </article>

    <article class="case" style="margin-top:16px">
      <h3 class="case-title">10X INCREASE IN MEMBERSHIP</h3>
      <p class="case-text" style="margin-top:13px">Greenway Paths Trust needed to move to online membership registration and contracted with Meridian Systems Corporation to build a significant online presence to engage potential members. Through compelling online tools and mobile applications, Greenway Paths has <em>increased membership 10 fold.</em></p>
    </article>

    <article class="case" style="margin-top:18px">
      <h3 class="case-title">20% REDUCTION IN OVERHEAD</h3>
      <p class="case-text" style="margin-top:13px">The National Council for Women's Equity had antiquated systems in place to manage over 500 chapters across the nation. Meridian Systems Corporation developed online tools to allow communication and management between the local chapters and national headquarters. This eliminated much of the overhead of chapter management, <em>reducing HR costs by 20%.</em></p>
    </article>
  </section>

</main>
</body>
</html>
```